Visit Qalimora Card (School That only teach arabic language) (Guaranteed Payment)

Hi, we are a new school That Teach arabic language in Tunisia, we are looking to conceptulize visit cards for our team. The business card will be printed in color and on Both Sides. We want to communiquer: innovation, excellence, professionalism, leadership and trust. Would we need the business card at the end with the details of everyone of our team (3) General and aussi has one for our center in Tunis. La même designed is used througout of course. Waiting for your sugestions! The address is the Sámi for all the visit cards: 47 Rue des Oliviers Zembra Cedar Building, 3rd Floor 1053 Les Berges du Lac 1, Tunisia aussi la même is the website for all www.qalimora.example The 4 visits Card Those names are: Karim Ouertani Jonas Freiberg Rania Gharbi Qalimora For Karim's Ouertani Visit Card Function name: Managing Partner Phone number: 216 94120386 Email: karim.ouertani@qalimora. example For Rania's visit card function name: Marketing Assistant Phone number: 216 97402615 Email: rania.gharbi@qalimora.example For Jonas's visit card: Function name: Managing Partner Phone number: 49 151 08246519 Mail: @ jonas.freiberg qalimora.example You can find our logo in the attachment.

```html
<!DOCTYPE html>
<html lang="fr">
<head>
<meta charset="utf-8">
<title>Qalimora – Carte de visite</title>
<link rel="stylesheet" href="https://fonts.googleapis.com/css2?family=Arimo:wght@400;700&display=swap">
<style>
  :root {
    --page-bg: #8f9090;
    --brand-blue: #0d4684;
    --panel-light: #e7e8eb;
    --text-light: #eef2f7;
    --text-soft: #d5deea;
  }
  * { box-sizing: border-box; margin: 0; padding: 0; }
  html, body {
    width: 1105px; height: 1200px; overflow: hidden;
    background: var(--page-bg);
    font-family: "Arimo", Arial, sans-serif;
  }
  .card {
    position: absolute; left: 182px;
    width: 747px; height: 427px;
    background: var(--brand-blue);
    overflow: hidden;
  }
  .card--front { top: 119px; }
  .card--back { top: 637px; }

  .logo-panel {
    position: absolute; top: 0; right: 0;
    width: 377px; height: 100%;
    background: var(--panel-light);
    border-radius: 86px 0 0 86px;
    display: flex; align-items: center; justify-content: center;
  }
  .wordmark {
    font-family: "Arimo", Arial, sans-serif;
    font-weight: 400; letter-spacing: 0.5px; line-height: 1;
  }
  .logo-panel .wordmark { color: var(--brand-blue); font-size: 72px; margin-top: -10px; }

  .contact-block { position: absolute; left: 33px; top: 86px; color: var(--text-light); }
  .person-name { font-weight: 700; font-size: 25px; letter-spacing: 0.6px; text-transform: uppercase; }
  .person-role { font-size: 19px; margin-top: 6px; color: var(--text-soft); }
  .address { font-size: 17.5px; line-height: 25px; margin-top: 22px; color: var(--text-soft); font-style: normal; }
  .contact-list { list-style: none; margin-top: 14px; font-size: 17.5px; color: var(--text-soft); }
  .contact-list li { display: flex; align-items: center; height: 29px; }
  .contact-list svg { width: 17px; height: 17px; margin-right: 11px; fill: var(--text-soft); flex: none; }

  .back-texture {
    position: absolute; inset: 0;
    background: linear-gradient(180deg, #114b89 0%, #0d4684 100%);
  }
  .card--back .wordmark {
    position: absolute; left: 0; right: 0; top: 158px;
    text-align: center; color: #ffffff; font-size: 96px;
  }
</style>
</head>
<body>
  <section class="card card--front" aria-label="Recto de la carte">
    <div class="contact-block">
      <h1 class="person-name">Karim Ouertani</h1>
      <p class="person-role">Managing Partner</p>
      <address class="address">
        47 Rue des Oliviers Zembra<br>
        Immeuble Cèdres, 3ème étage<br>
        2046 Jardins de Carthage,Tunisie
      </address>
      <ul class="contact-list">
        <li>
          <svg viewBox="0 0 24 24" aria-hidden="true"><path d="M6.6 10.8a15.1 15.1 0 0 0 6.6 6.6l2.2-2.2c.3-.3.7-.4 1-.2 1.1.4 2.3.6 3.6.6.6 0 1 .4 1 1V20c0 .6-.4 1-1 1A17 17 0 0 1 3 4c0-.6.4-1 1-1h3.5c.6 0 1 .4 1 1 0 1.3.2 2.5.6 3.6.1.3 0 .7-.2 1z"/></svg>
          +216 94 120 386
        </li>
        <li>
          <svg viewBox="0 0 24 24" aria-hidden="true"><path d="M2 5h20v14H2zm2 2v.4l8 5 8-5V7zm0 2.8V17h16V9.8l-8 5z"/></svg>
          karim.ouertani@qalimora.example
        </li>
        <li>
          <svg viewBox="0 0 24 24" aria-hidden="true"><path d="M12 2a10 10 0 1 0 0 20 10 10 0 0 0 0-20zm-1 17.9A8 8 0 0 1 4.1 10.5L9 15v1c0 1.1.9 2 2 2zm6.9-2.5c-.3-.8-1-1.4-1.9-1.4h-1v-3c0-.6-.4-1-1-1H8v-2h2c.6 0 1-.4 1-1V7h2c1.1 0 2-.9 2-2v-.4a8 8 0 0 1 2.9 12.8z"/></svg>
          www.qalimora.example
        </li>
      </ul>
    </div>
    <div class="logo-panel">
      <span class="wordmark">qalimora</span>
    </div>
  </section>

  <section class="card card--back" aria-label="Verso de la carte">
    <div class="back-texture" role="img" aria-label="Fond bleu avec motif discret répétant le nom de l'école"></div>
    <span class="wordmark">qalimora</span>
  </section>
</body>
</html>
```